Property Restoration Company needs a tri-fold brochure

We work in the water damage industry, when there is emergency flooding in peoples homes or businesses. We would like to have a cover page, inside with the info about the services we provide, which includes water damage, sewage clean-up, and mold remediation. Our message is that we are professional, prompt, and reassuring to people that may be in crisis.

Our brochures are aimed for property management but would like to keep it vague
We would like to use pictures or graphics that INSINUATE the hazardous materials clean-up, without actually having gross pictures of the line of work we are in.

At least one of the graphics should include using drying equipment inside a residential home. We use blue equipment and use a blue calming color for our brand.

The mood of the brochure should be reassuring and cheery demeanor.

There should be imagery pertaining to 24/7 emergency service 365 days a year, with a 60-90 minute response time.

On the back of the middle page should be a section that has our address, phone number, email and website

Target Market(s)

Property Management, Homeowners, Business Owners

Industry/Entity Type

Construction/Demo/Restoration

Colors
0094D4
00A9DD
6FCCEA
C7EBF8
E9F6FB

Requirements
Must have
• 24/7 Emergency Response, 365 Days a year, contact information, branding, reassuring demeanor
Nice to have
• Graphics that start with flooding -> clean-up -> drying -> to things back to normal
Should not have
• Images or graphics that depict sewage, insinuation only

```html
<!DOCTYPE html>
<html lang="en">
<head>
<meta charset="utf-8">
<title>Tidewell Restoration – Tri-fold Brochure</title>
<link href="https://fonts.googleapis.com/css2?family=Montserrat:wght@400;500;600;700;800;900&display=swap" rel="stylesheet">
<style>
  :root{
    --ink:#333a40;
    --blue-deep:#1f7fb0;
    --blue:#2a97c8;
    --blue-bright:#0094d4;
    --blue-soft:#8ecdf7;
    --blue-pale:#deeefb;
    --blue-mist:#e9f6fb;
    --white:#ffffff;
    --stage:#000000;
  }
  *{box-sizing:border-box;margin:0;padding:0}
  html,body{width:857px;height:1200px;overflow:hidden;background:var(--stage)}
  body{position:relative;font-family:"Montserrat",sans-serif;color:var(--ink)}
  .sheet{position:absolute;left:43px;width:772px;height:578px;overflow:hidden}
  .sheet--outside{top:13px;background:var(--white)}
  .sheet--inside{top:605px;background:var(--blue-pale)}
  .sheet svg.waves{position:absolute;left:0;top:0;width:772px;height:578px}
  .abs{position:absolute}
  .photo-panel{position:absolute;left:515px;top:0;width:257px;height:578px;
    background:linear-gradient(160deg,#e7ecef 0%,#cfd8de 40%,#b9c2c8 70%,#8e969c 100%)}
  .rule{position:absolute;height:2px;width:36px;background:var(--blue)}
  .headline{left:14px;top:401px;font-weight:900;font-size:22.5px;line-height:27px;letter-spacing:.3px;color:var(--ink);width:250px}
  .headline .accent{color:var(--blue-deep)}
  .subline{left:14px;top:488px;font-weight:800;font-size:18px;line-height:23px;color:var(--blue-deep);letter-spacing:.2px}
  .contact-title{left:257px;width:258px;top:148px;text-align:center;font-weight:700;font-size:19.5px;letter-spacing:.8px;color:var(--ink)}
  .brand-mark{border-radius:50%;background:var(--blue)}
  .brand-name{font-weight:700;letter-spacing:-.2px;text-align:center;white-space:nowrap}
  .brand-phone{font-weight:700;text-align:center}
  .brand-services{font-weight:700;text-align:center;letter-spacing:1.6px;white-space:nowrap}
  .contact-list{left:301px;top:294px;list-style:none}
  .contact-list li{display:flex;align-items:center;height:32px;margin-bottom:1px}
  .contact-list svg{width:23px;height:23px;flex:none;margin-right:6px}
  .contact-list span{font-size:9px;line-height:13px;font-weight:500;letter-spacing:.3px;color:var(--ink)}
  .contact-list .big{font-size:12px}
  .section-title{font-weight:700;font-size:20px;letter-spacing:.6px;line-height:24px;color:var(--ink)}
  .about-title{left:14px;top:318px;width:238px}
  .service-title{font-weight:700;font-size:16px;letter-spacing:.6px;color:var(--blue-deep);white-space:nowrap}
  .copy{font-size:10px;line-height:17px;color:var(--ink);letter-spacing:.1px}
  .copy--justify{text-align:justify}
  .service-photo{position:absolute;width:226px;height:98px;border-radius:2px}
</style>
</head>
<body>

<!-- Outside sheet -->
<section class="sheet sheet--outside">
  <div class="photo-panel" role="img" aria-label="Photo: technician in a white shirt and yellow work trousers cleaning a wet floor inside a bright home"></div>

  <svg class="waves" viewBox="0 0 772 578">
    <defs>
      <clipPath id="leftPanel"><rect x="0" y="0" width="257" height="578"/></clipPath>
      <linearGradient id="callCentre" x1="0" y1="0" x2="1" y2="1">
        <stop offset="0" stop-color="#e9eef1"/><stop offset=".45" stop-color="#9fb3c2"/><stop offset=".8" stop-color="#2f5f98"/><stop offset="1" stop-color="#1d3e6c"/>
      </linearGradient>
    </defs>
    <g fill="none" stroke="var(--blue-mist)" stroke-width="14" opacity=".9">
      <circle cx="160" cy="470" r="95"/><circle cx="400" cy="330" r="110"/>
    </g>
    <g clip-path="url(#leftPanel)">
      <circle cx="150" cy="236" r="146" fill="var(--blue-soft)"/>
      <circle cx="146" cy="222" r="140" fill="var(--blue)"/>
      <g role="img" aria-label="Photo: smiling customer service team wearing headsets at a call centre">
        <circle cx="136" cy="200" r="131" fill="url(#callCentre)"/>
      </g>
    </g>
    <path d="M0,0 H515 V160 C495,75 455,38 395,42 C310,48 210,118 128,122 C62,125 22,100 0,70 Z" fill="var(--blue)"/>
    <path d="M0,78 C22,108 62,133 128,130 C210,126 310,56 395,50 C452,46 492,80 512,150" fill="none" stroke="var(--white)" stroke-width="3"/>
    <path d="M257,578 V400 C282,480 322,540 392,540 C462,540 562,440 652,440 C712,440 750,470 772,496 V578 Z" fill="var(--blue)"/>
    <path d="M262,420 C290,492 330,532 392,532 C462,532 562,430 652,430 C712,430 752,462 772,486" fill="none" stroke="var(--white)" stroke-width="3"/>
    <rect x="0" y="548" width="257" height="30" fill="var(--white)"/>
  </svg>

  <h2 class="abs headline"><span class="accent">24/7 EMERGENCY SERVICE</span> 365 DAYS A YEAR</h2>
  <p class="abs subline">With a 60-90 minute<br>response time.</p>
  <div class="rule" style="left:14px;top:549px"></div>

  <h2 class="abs contact-title">CONTACT US</h2>
  <div class="rule" style="left:368px;top:180px"></div>
  <div class="abs brand-mark" style="left:373px;top:193px;width:26px;height:26px"></div>
  <p class="abs brand-name" style="left:257px;width:258px;top:226px;font-size:11.5px;color:var(--blue-deep)">TIDEWELL RESTORATION</p>
  <p class="abs brand-phone" style="left:257px;width:258px;top:245px;font-size:7.5px;color:var(--blue-deep)">1 (800) 555-0142</p>
  <p class="abs brand-services" style="left:257px;width:258px;top:262px;font-size:7px;color:var(--blue-soft)">WATER &nbsp;•&nbsp; SEWAGE &nbsp;•&nbsp; MOLD</p>

  <ul class="abs contact-list">
    <li>
      <svg viewBox="0 0 24 24"><circle cx="12" cy="12" r="12" fill="var(--blue)"/><path d="M12 6.5a3.6 3.6 0 0 0-3.6 3.6c0 2.7 3.6 6.9 3.6 6.9s3.6-4.2 3.6-6.9A3.6 3.6 0 0 0 12 6.5zm0 4.9a1.3 1.3 0 1 1 0-2.6 1.3 1.3 0 0 1 0 2.6z" fill="var(--white)"/></svg>
      <span>48 Harbor Lane Suite 210,<br>Portland 97201, United States</span>
    </li>
    <li>
      <svg viewBox="0 0 24 24"><circle cx="12" cy="12" r="12" fill="var(--blue)"/><path d="M9.2 7.2l1.4 2.4-.9 1.1c.6 1.3 1.5 2.2 2.7 2.8l1.1-.9 2.3 1.4-.6 1.9c-3.9.1-7.6-3.6-7.6-7.6z" fill="var(--white)"/></svg>
      <span class="big">1 (800) 555-0142</span>
    </li>
    <li>
      <svg viewBox="0 0 24 24"><circle cx="12" cy="12" r="12" fill="var(--blue)"/><rect x="6.5" y="8" width="11" height="8" rx="1" fill="var(--white)"/><path d="M6.8 8.4L12 12.4l5.2-4" fill="none" stroke="var(--blue)" stroke-width="1"/></svg>
      <span>hello@tidewellrestore.com</span>
    </li>
    <li>
      <svg viewBox="0 0 24 24"><circle cx="12" cy="12" r="12" fill="var(--blue)"/><g fill="none" stroke="var(--white)" stroke-width="1.1"><circle cx="12" cy="12" r="5.5"/><ellipse cx="12" cy="12" rx="2.3" ry="5.5"/><path d="M6.5 12h11M7.3 9.3h9.4M7.3 14.7h9.4"/></g></svg>
      <span>www.tidewellrestore.com</span>
    </li>
  </ul>

  <div class="abs brand-mark" style="left:627px;top:458px;width:34px;height:34px;background:var(--white)"></div>
  <p class="abs brand-name" style="left:515px;width:257px;top:500px;font-size:16.5px;color:var(--white)">TIDEWELL RESTORATION</p>
  <p class="abs brand-phone" style="left:515px;width:257px;top:528px;font-size:11px;color:var(--white)">1 (800) 555-0142</p>
  <p class="abs brand-services" style="left:515px;width:257px;top:552px;font-size:10px;letter-spacing:2.2px;color:var(--white)">WATER &nbsp;•&nbsp; SEWAGE &nbsp;•&nbsp; MOLD</p>
</section>

<!-- Inside sheet -->
<section class="sheet sheet--inside">
  <svg class="waves" viewBox="0 0 772 578">
    <defs>
      <clipPath id="aboutPanel"><rect x="0" y="0" width="257" height="578"/></clipPath>
      <linearGradient id="floodCrew" x1="0" y1="0" x2="0" y2="1">
        <stop offset="0" stop-color="#9fb1bd"/><stop offset=".45" stop-color="#6c7f88"/><stop offset=".7" stop-color="#a8875a"/><stop offset="1" stop-color="#3a4a54"/>
      </linearGradient>
    </defs>
    <rect x="257" y="0" width="515" height="578" fill="#e2f0fc"/>
    <g fill="none" stroke="#d2e6f6" stroke-width="16">
      <circle cx="140" cy="470" r="90"/><circle cx="420" cy="300" r="120"/><circle cx="650" cy="360" r="110"/>
    </g>
    <g clip-path="url(#aboutPanel)">
      <circle cx="150" cy="160" r="148" fill="var(--blue-soft)"/>
      <circle cx="146" cy="146" r="140" fill="var(--blue)"/>
      <g role="img" aria-label="Photo: crew in hard hats and high-visibility gear pumping out a flooded industrial basement">
        <circle cx="142" cy="133" r="133" fill="url(#floodCrew)"/>
      </g>
    </g>
    <path d="M0,0 H88 C48,18 18,50 0,92 Z" fill="var(--blue)"/>
    <path d="M0,100 C20,56 52,22 96,0" fill="none" stroke="var(--white)" stroke-width="3"/>
    <path d="M257,0 H772 V18 C712,60 620,70 520,60 C430,50 350,14 300,2 Z" fill="var(--blue)"/>
    <path d="M350,0 C410,22 470,48 540,58 C630,72 720,50 772,18" fill="none" stroke="var(--white)" stroke-width="3"/>
    <path d="M0,578 V560 C120,520 260,500 360,510 C500,525 600,578 700,560 C740,550 760,530 772,510 V578 Z" fill="var(--blue)"/>
    <path d="M0,552 C120,512 260,492 360,502 C500,517 600,568 700,552" fill="none" stroke="var(--white)" stroke-width="3"/>
  </svg>

  <h2 class="abs section-title about-title">ABOUT<br>TIDEWELL<br>RESTORATION</h2>
  <div class="rule" style="left:14px;top:397px"></div>
  <p class="abs copy" style="left:14px;top:411px;width:240px">Duis mollis, est non commodo luctus, nisi erat porttitor ligula, eget lacinia odio sem nec elit. Morbi leo risus, porta ac consectetur ac, vestibu lum at eros. Nulla vitae elit libero, a pharetra augue.</p>

  <h2 class="abs section-title" style="left:271px;top:74px">OUR SERVICES</h2>
  <div class="rule" style="left:271px;top:108px"></div>
  <p class="abs copy copy--justify" style="left:271px;top:119px;width:233px">Sed ut perspiciatis unde omnis iste natus error sit voluptatem accusantium doloremque laudantium, totam rem aperiam, eaque ipsa quae ab illo inventore veritatis et quasi architecto beatae vitae dicta sunt explicabo. Nemo enim ipsam voluptatem quia voluptas sit aspernatur aut odit aut fugit, sed quia consequuntur magni dolores eos qui ratione voluptatem sequi nesciunt.</p>

  <div class="service-photo" style="left:274px;top:289px;background:linear-gradient(90deg,#8d949b 0%,#d9d6cf 45%,#c9c3b8 75%,#3a2e26 100%)" role="img" aria-label="Photo: technician inspecting water-stained wall plaster near the skirting board"></div>
  <h3 class="abs service-title" style="left:271px;top:397px">WATER DAMAGE</h3>
  <div class="rule" style="left:271px;top:424px"></div>
  <p class="abs copy" style="left:271px;top:432px;width:236px">Duis mollis, est non commodo luctus, nisi erat porttitor ligula, eget lacinia odio sem nec elit. Morbi leo risus, porta ac consectetur ac, vestibu lum at eros.</p>

  <div class="service-photo" style="left:530px;top:85px;background:linear-gradient(180deg,#8e8a78 0%,#6f6e55 45%,#b8c0c2 70%,#4f5a44 100%)" role="img" aria-label="Photo: outflow pipe releasing water into a concrete channel"></div>
  <h3 class="abs service-title" style="left:527px;top:193px">SEWAGE CLEAN-UP</h3>
  <div class="rule" style="left:527px;top:220px"></div>
  <p class="abs copy" style="left:527px;top:229px;width:236px">Duis mollis, est non commodo luctus, nisi erat porttitor ligula, eget lacinia odio sem nec elit. Morbi leo risus, porta ac consectetur ac, vestibu lum at eros.</p>

  <div class="service-photo" style="left:530px;top:306px;background:linear-gradient(90deg,#6f7f78 0%,#d9dde0 35%,#8a9891 65%,#76857f 100%)" role="img" aria-label="Photo: worker in a white protective suit spraying treatment onto a wall"></div>
  <h3 class="abs service-title" style="left:527px;top:421px">MOLD REMEDIATION</h3>
  <div class="rule" style="left:527px;top:448px"></div>
  <p class="abs copy" style="left:527px;top:458px;width:236px">Duis mollis, est non commodo luctus, nisi erat porttitor ligula, eget lacinia odio sem nec elit. Morbi leo risus, porta ac consectetur ac, vestibu lum at eros.</p>
</section>

</body>
</html>
```